QVB Commercial Roof Restoration LLC needs billboard and banner designs

Need billboard ad design for small commercial roof restoration company. Looking for a billboard design that can be used on digital and hard print billboards. Also need banner design for 4' x 8' job site banners that will go by roadside to draw potential customers to our brand. Our vision for bill board would show an attractive women in business dress, clearly in a building having to use an (red) umbrella (inside building) due to leaking roof. Caption "WE CAN HELP" www.QVBCOMMERCIALROOF.example
For banner design we would use some before/after roof photos (attached, blend/overlay at an angle) in background with "Another Quality Commercial Roof Restoration By:" "QVB Commercial Roof LLC" "Is your commercial roof leaking? Call 555.314.0827 for help".
All final designs should communicate commercial roof restoration only.
Target Market(s)
Commercial building owner/managers
Industry/Entity Type
Roofing
Requirements
Must have
- Just added a Jpeg file of a logo of the company that we buy our products from. This logo & "Certified Premier Installers" needs to be added to the project. It only needs to have a small footprint on the ad. Contact me if you have questions. Thank you.
Nice to have
- Billboard design; our name, website, relay our message with image. As described above in project description
Banner; Our name, phone number and bold written message

```html
<!DOCTYPE html>
<html lang="en">
<head>
<meta charset="utf-8">
<title>QVB Commercial Roof Restoration – Billboard</title>
<link href="https://fonts.googleapis.com/css2?family=Montserrat:wght@500;600;700;800;900&display=swap" rel="stylesheet">
<style>
  :root {
    --page: #ffffff;
    --brand-red: #d71f2b;
    --brand-blue: #1d3a93;
    --deep-blue: #142c7a;
    --ink: #2a2a2e;
    --silver: #c9ccd2;
    --panel: #f4f5f7;
  }
  * { margin: 0; padding: 0; box-sizing: border-box; }
  html, body {
    width: 836px; height: 1200px; overflow: hidden;
    background: var(--page);
    font-family: "Montserrat", Arial, sans-serif;
  }
  .billboard {
    position: absolute;
    left: 48px; top: 415px;
    width: 740px; height: 370px;
    overflow: hidden;
    box-shadow: 0 10px 18px rgba(0,0,0,0.25);
  }
  .billboard-art { position: absolute; inset: 0; width: 100%; height: 100%; }
  .brand-name {
    position: absolute; left: 35px; top: 26px;
    display: flex; align-items: center; gap: 8px;
    color: var(--brand-blue);
    font-weight: 800; font-size: 19px; line-height: 1.05;
    letter-spacing: 0.2px;
  }
  .brand-mark { width: 14px; height: 14px; border-radius: 50%; background: var(--brand-blue); flex: none; }
  .brand-name small { display: block; font-size: 11.5px; font-weight: 800; }
  .headline-lead {
    position: absolute; left: 35px; top: 117px;
    font-size: 17.5px; font-weight: 600; color: var(--ink); letter-spacing: 0.1px;
  }
  .headline-main {
    position: absolute; left: 32px; top: 132px;
    font-size: 54px; font-weight: 900; color: var(--brand-red); letter-spacing: -0.5px;
  }
  .web-button {
    position: absolute; left: 36px; top: 191px;
    width: 280px; height: 30px;
    border-radius: 5px;
    background: linear-gradient(#3b5fc4, var(--deep-blue));
    box-shadow: 0 4px 6px rgba(0,0,0,0.3);
    color: #fff; font-size: 12.5px; font-weight: 700;
    display: flex; align-items: center; justify-content: center;
  }
  .phone {
    position: absolute; left: 35px; top: 319px;
    display: flex; align-items: center; gap: 6px;
    color: #fff; font-size: 29px; font-weight: 800;
  }
  .phone svg { width: 28px; height: 28px; }
</style>
</head>
<body>
<section class="billboard">
  <svg class="billboard-art" viewBox="0 0 740 370" preserveAspectRatio="none">
    <defs>
      <linearGradient id="panelFade" x1="0" y1="0" x2="1" y2="1">
        <stop offset="0" stop-color="#ffffff"/>
        <stop offset="1" stop-color="#e7e9ed"/>
      </linearGradient>
      <linearGradient id="photoTone" x1="0" y1="0" x2="1" y2="1">
        <stop offset="0" stop-color="#d9d8d4"/>
        <stop offset="0.5" stop-color="#e8d9b8"/>
        <stop offset="1" stop-color="#f2ead8"/>
      </linearGradient>
      <linearGradient id="silverSweep" x1="0" y1="0" x2="1" y2="0">
        <stop offset="0" stop-color="#f4f4f6"/>
        <stop offset="0.5" stop-color="#b9bcc3"/>
        <stop offset="1" stop-color="#eceef1"/>
      </linearGradient>
    </defs>
    <rect class="panel-bg" width="740" height="370" fill="url(#panelFade)"/>
    <path class="silver-sweep" d="M0,240 Q220,330 430,270 L430,282 Q220,342 0,252 Z" fill="url(#silverSweep)"/>
    <path class="blue-band" d="M0,258 Q220,335 440,282 L520,370 L0,370 Z" fill="var(--brand-blue)"/>
    <path class="red-swoosh" d="M400,0 C325,120 340,290 475,370 L505,370 C370,290 360,120 420,0 Z" fill="var(--brand-red)"/>
    <path class="silver-edge" d="M420,0 C360,120 370,290 505,370 L515,370 C385,290 378,120 432,0 Z" fill="var(--silver)"/>
    <path class="photo-area" role="img" aria-label="Photo: businesswoman in a dark suit holding a red umbrella inside an office building with water-stained leaking ceiling tiles"
      d="M432,0 C378,120 385,290 515,370 L740,370 L740,0 Z" fill="url(#photoTone)"/>
  </svg>

  <div class="brand-name">
    <span class="brand-mark"></span>
    <span>QVB COMMERCIAL<small>ROOF RESTORATION</small></span>
  </div>
  <p class="headline-lead">IS YOUR COMMERCIAL ROOF</p>
  <h1 class="headline-main">LEAKING?</h1>
  <div class="web-button">www.QVBCOMMERCIALROOF.example</div>
  <div class="phone">
    <svg viewBox="0 0 28 28" aria-hidden="true">
      <circle cx="14" cy="14" r="12.5" fill="none" stroke="#fff" stroke-width="2"/>
      <path d="M10 7.5l2.5 3-1.6 1.8c.9 2 2.4 3.6 4.4 4.6l1.8-1.6 3 2.4-1.6 2.6c-5.2-.6-9.8-5.1-10.5-10.4z" fill="#fff"/>
    </svg>
    <span>555.314.0827</span>
  </div>
</section>
</body>
</html>
```